WWW.VELTRONA.IT BUSINNES CARD

WE NEED A BUSINESS CARD . I HAVE A COMPANY IN ITALY NR 1 IN HAIR MEDICAL CARE AN HAIR REPLECEMENT . IN CARD I NEED WRITE WEB ADDRESS, MAIL , ADDRESS, TELEPHONE NUMBER , AND NAME
IN THE BACK SIDE I NEED MY DOCTOR LOGO .
MY WEB SITE IS WWW.VELTRONA.IT
Updates

Target Market(s)

CONSUMER B2C

Industry/Entity Type

Hair And Beauty

Contact Information for Business Card

I WANT A MEDICAL BUSINESS CARD.

Font styles to use
Other font styles liked:
• VERDANA

Colors
33a6d7
3176b5
85abd2
aedbee
eaf1f7
ffffff

Requirements
Must have
• I NEED MY LOGO AND LOGO OF DR VELTRONA

```html
<!DOCTYPE html>
<html lang="it">
<head>
<meta charset="utf-8">
<title>Veltrona – Business Card</title>
<link href="https://fonts.googleapis.com/css2?family=Open+Sans:ital,wght@0,400;0,600;0,700;1,700&display=swap" rel="stylesheet">
<style>
  :root {
    --sky: #33a6d7;
    --navy: #2f5d9a;
    --blue: #3176b5;
    --deep: #275a96;
    --soft: #85abd2;
    --ice: #aedbee;
    --mist: #eaf1f7;
    --white: #ffffff;
    --stage: #ececec;
    --art-top: #9c7a6a;
    --art-bottom: #d9c2b4;
  }
  * { margin: 0; padding: 0; box-sizing: border-box; }
  html, body { width: 1200px; height: 1000px; overflow: hidden; }
  body {
    background: var(--stage);
    font-family: "Open Sans", Verdana, sans-serif;
    position: relative;
  }
  .card {
    position: absolute;
    left: 313px;
    width: 574px;
    height: 327px;
    overflow: hidden;
    box-shadow: 0 2px 8px rgba(0,0,0,0.12);
  }
  .card--front { top: 140px; background: var(--white); }
  .card--back {
    top: 532px;
    background: linear-gradient(100deg, #2a5a97 0%, #2d5d99 20%, #5a86ba 50%, #86afd6 80%, #8fc0e2 100%);
  }

  /* front */
  .brand-name {
    position: absolute; left: 42px; top: 44px;
    font-size: 56px; font-weight: 600; color: var(--navy);
    line-height: 1;
  }
  .tagline {
    position: absolute; left: 47px; top: 121px;
    font-size: 17px; color: var(--navy); letter-spacing: 0.2px;
  }
  .wave { position: absolute; left: 0; top: 150px; }
  .person { position: absolute; left: 46px; top: 205px; }
  .person__name { font-size: 26.5px; color: var(--navy); line-height: 1; }
  .person__role { font-size: 18.5px; color: var(--sky); margin-top: 13px; }
  .contacts { position: absolute; left: 253px; top: 205px; list-style: none; }
  .contacts li {
    display: flex; align-items: center; gap: 7px;
    color: var(--navy); height: 22px; white-space: nowrap;
  }
  .contacts li + li { margin-top: 19px; }
  .contacts .address { font-size: 18.5px; }
  .contacts .phone { font-size: 23px; }
  .contacts .email { font-size: 17.5px; letter-spacing: 2.5px; }
  .contacts svg { flex: none; }

  /* back */
  .website {
    position: absolute; left: 31px; top: 197px;
    color: var(--white); font-size: 28px; font-weight: 700; font-style: italic;
    letter-spacing: 6.5px; white-space: nowrap;
  }
  .mascot-art {
    position: absolute; left: 404px; top: 14px;
    width: 112px; height: 304px;
    border-radius: 6px;
    background: linear-gradient(180deg, var(--art-top) 0%, var(--art-bottom) 100%);
    opacity: 0.85;
  }
  .doctor-name {
    position: absolute; left: 522px; top: 273px;
    transform: rotate(-90deg); transform-origin: left top;
    color: var(--deep); font-size: 17px; font-weight: 700; font-style: italic;
    white-space: nowrap;
  }
</style>
</head>
<body>

<section class="card card--front" aria-label="Fronte del biglietto">
  <div class="brand-name">Veltrona</div>
  <div class="tagline">CURA E REINTEGRAZIONE DEI CAPELLI</div>
  <svg class="wave" width="574" height="40" viewBox="0 0 574 40" aria-hidden="true">
    <path d="M20 26 C120 6 200 22 260 30 C320 38 360 36 393 16" fill="none" stroke="var(--sky)" stroke-width="2.5"/>
  </svg>

  <div class="person">
    <div class="person__name">NAME HERE</div>
    <div class="person__role">DOCTOR</div>
  </div>

  <ul class="contacts">
    <li class="address">
      <svg width="16" height="18" viewBox="0 0 16 18" aria-hidden="true"><path d="M8 1a6 6 0 0 0-6 6c0 4.5 6 10 6 10s6-5.5 6-10a6 6 0 0 0-6-6z" fill="var(--sky)"/><circle cx="8" cy="7" r="2.2" fill="var(--white)"/></svg>
      VIA DEI TIGLI 18, VERONA, ITALY
    </li>
    <li class="phone">
      <svg width="17" height="17" viewBox="0 0 17 17" aria-hidden="true"><rect x="1" y="2" width="15" height="14" rx="1.5" fill="var(--sky)"/><rect x="3" y="4" width="3" height="10" fill="var(--white)"/><g fill="var(--white)"><rect x="8" y="5" width="2" height="2"/><rect x="11" y="5" width="2" height="2"/><rect x="8" y="8.5" width="2" height="2"/><rect x="11" y="8.5" width="2" height="2"/><rect x="8" y="12" width="2" height="2"/><rect x="11" y="12" width="2" height="2"/></g></svg>
      +3904 5550 173
    </li>
    <li class="email">
      <svg width="17" height="13" viewBox="0 0 17 13" aria-hidden="true"><rect x="0.5" y="0.5" width="16" height="12" fill="var(--sky)"/><path d="M1 1l7.5 6.5L16 1" fill="none" stroke="var(--white)" stroke-width="1.3"/></svg>
      info@veltrona.it
    </li>
  </ul>
</section>

<section class="card card--back" aria-label="Retro del biglietto">
  <div class="website">www.veltrona.it</div>
  <div class="mascot-art" role="img" aria-label="Illustrazione della mascotte del dottore con camice bianco"></div>
  <div class="doctor-name">dr. Veltrona</div>
</section>

</body>
</html>
```